Website Design for Professional Services Company

• Create a new website design that is easy to maintain inside of WordPress with a main page design, a design for generic content pages, and a design for customer case studies. Our current design relies on a number of plugins to function, and we would like to get away from that as much as possible. Our current design also requires a fair amount of coding that we would like to get away from. The more we can use native WordPress the better. We are not opposed to a small subset of plugins that are widely used and readily updated. Our current website can be found at https://tarnwickconsulting.com/. Our fonts (for use in graphics, we don’t want custom fonts on the website itself to make sure it always displays correctly) and colors are as follows:
o Tarnwick Blue:
 #1b75bc
o Tarnwick Grey:
 #6d6f71
o Main Font:
 Telegrafico
o Accent Font:
 Nexa Light

```html
<!DOCTYPE html>
<html lang="en">
<head>
<meta charset="utf-8">
<title>Tarnwick Consulting</title>
<link href="https://fonts.googleapis.com/css2?family=League+Spartan:wght@300;400;500;600;700&family=Lato:wght@400;700&family=Poppins:wght@400;500;600&display=swap" rel="stylesheet">
<style>
:root{
  --blue:#1b75bc;
  --blue-mid:#2a7fd0;
  --grey:#6d6f71;
  --navy:#0f2352;
  --ink:#1c1f3a;
  --text:#44474f;
  --pale:#f0f4f8;
  --white:#ffffff;
  --foot-bar:#1c5aa3;
}
*{margin:0;padding:0;box-sizing:border-box}
html,body{width:1200px;height:3664px;overflow:hidden;background:var(--white)}
body{position:relative;font-family:'Lato',sans-serif;color:var(--text)}
.abs{position:absolute}
.head{font-family:'League Spartan',sans-serif;color:var(--ink)}
.btn{position:absolute;background:var(--blue);color:var(--white);font-family:'Poppins',sans-serif;font-weight:600;font-size:14px;display:flex;align-items:center;justify-content:center;gap:8px;border-radius:2px;letter-spacing:.2px}
.rule{position:absolute;height:2px;background:var(--blue)}
.brand{position:absolute;display:flex;align-items:center;gap:10px;font-family:'League Spartan',sans-serif;font-weight:600;color:var(--blue)}
.brand i{display:block;background:var(--blue)}

.topbar{left:0;top:0;width:1200px;height:46px;background:#f7f8fa}
.topbar .phone{left:90px;top:14px;font-size:15px;color:#444;display:flex;gap:8px;align-items:center}
.topbar .tools{right:90px;top:14px;display:flex;gap:14px;color:#555;font-size:13px}

.hero-photo{left:420px;top:46px;width:780px;height:600px}
.nav{top:80px;display:flex;gap:0}
.nav a{position:absolute;font-family:'League Spartan',sans-serif;font-size:18px;color:var(--white);text-decoration:none;white-space:nowrap}
.cta{left:938px;top:71px;width:174px;height:39px;background:var(--white);border-radius:20px;color:var(--blue);font-family:'League Spartan',sans-serif;font-size:17px;display:flex;align-items:center;justify-content:center}
.hero-title{left:94px;top:230px;font-size:48px;line-height:50px;font-weight:300}
.hero-title b{font-weight:700}
.hero-copy{left:94px;top:408px;width:420px;font-family:'League Spartan',sans-serif;font-size:17px;line-height:28px;color:#3a3f5a}

.why-title{left:178px;top:750px;font-size:40px;font-weight:400}
.why-title b{font-weight:700}
.why-copy{left:178px;top:834px;width:405px;font-size:14.5px;line-height:23.3px;color:#3a3a3a}
.why-art{left:690px;top:725px;width:334px;height:375px;border-radius:18px;background:linear-gradient(160deg,#0d2d55,#1f6fb4 45%,#3a87c8 70%,#e8a36a);}
.why-shadow{left:660px;top:1095px;width:400px;height:30px;background:radial-gradient(ellipse at center,rgba(0,0,0,.18),transparent 70%)}

.services{left:0;top:1230px;width:1200px;height:690px}
.svc-title{left:0;top:1372px;width:1200px;text-align:center;font-family:'League Spartan',sans-serif;font-size:38px;color:var(--white)}
.card{position:absolute;top:1496px;width:270px;height:284px;background:var(--white);box-shadow:0 6px 18px rgba(0,0,0,.15);text-align:center}
.card svg{display:block;margin:24px auto 0}
.card h3{font-family:'Poppins',sans-serif;font-weight:500;font-size:17px;color:var(--ink);margin-top:18px}
.card p{font-size:13.5px;line-height:19.5px;color:#555;margin:14px 22px 0}
.card.dark{background:linear-gradient(180deg,#3a3f4a,#2a2e38)}
.card.dark h3,.card.dark p{color:var(--white)}
.card.dark p{font-weight:700}

.values-bg{left:0;top:1920px;width:1200px;height:640px}
.values-title{left:0;top:2028px;width:1200px;text-align:center;font-family:'Poppins',sans-serif;font-size:36px;line-height:46px;color:var(--ink)}
.val{position:absolute;width:200px}
.val h4{font-family:'Poppins',sans-serif;font-weight:400;font-size:20px;color:var(--ink)}
.val p{font-size:14px;line-height:20px;color:#555;margin-top:4px}
.val.r{text-align:right}

.blog-title{left:0;top:2585px;width:1200px;text-align:center;font-size:38px;font-weight:400}
.blog-title b{font-weight:700}
.post{position:absolute;top:2685px;width:270px;height:420px}
.post .img{position:absolute;left:0;top:0;width:270px;height:230px}
.post .badge{position:absolute;left:210px;top:9px;width:46px;height:46px;border-radius:50%;background:var(--blue);color:var(--white);font-family:'Poppins',sans-serif;font-size:10px;font-weight:600;line-height:11px;display:flex;align-items:center;justify-content:center;text-align:center}
.post .body{position:absolute;left:11px;top:173px;width:248px;height:245px;background:var(--white);border:1px solid #e2e4ea;border-radius:0 0 6px 6px;padding:26px 22px 0}
.post h5{font-family:'Poppins',sans-serif;font-weight:600;font-size:13px;line-height:19px;color:var(--ink);text-transform:uppercase}
.post .by{font-family:'Poppins',sans-serif;font-style:italic;font-size:12.5px;color:#333;margin-top:12px;display:flex;gap:7px;align-items:center}
.post p{font-size:13.5px;line-height:20px;color:#555;margin-top:8px}
.post .more{position:absolute;left:23px;top:179px;width:126px;height:35px;border:1.5px solid var(--blue);border-radius:18px;color:var(--blue);font-family:'Poppins',sans-serif;font-weight:600;font-size:11px;display:flex;align-items:center;justify-content:center;gap:6px}

.footer{left:0;top:3211px;width:1200px;height:370px;background:var(--navy)}
.foot-bar{left:0;top:3581px;width:1200px;height:83px;background:var(--foot-bar);color:#dfe8f5;font-family:'League Spartan',sans-serif;font-size:15px;text-align:center;padding-top:30px}
.social{position:absolute;top:3457px;width:32px;height:32px;border:1.5px solid #fff;border-radius:50%}
.f-h{font-family:'Poppins',sans-serif;font-weight:600;font-size:16px;color:var(--white);letter-spacing:.3px}
.f-links a{position:absolute;left:489px;font-family:'League Spartan',sans-serif;font-size:18px;color:#cfd6e6;text-decoration:none}
.f-copy{left:744px;top:3318px;width:300px;font-size:13px;line-height:23px;color:#b8c1d6}
.f-input{left:744px;top:3382px;width:283px;height:34px;background:var(--white);border-radius:2px;font-size:13px;color:#555;padding:9px 16px}
</style>
</head>
<body>

<div class="abs topbar">
  <div class="abs phone">
    <svg width="16" height="16" viewBox="0 0 24 24"><path fill="#1b75bc" d="M6.6 10.8a15 15 0 0 0 6.6 6.6l2.2-2.2c.3-.3.7-.4 1-.2 1.1.4 2.3.6 3.6.6.6 0 1 .4 1 1V20c0 .6-.4 1-1 1A17 17 0 0 1 3 4c0-.6.4-1 1-1h3.5c.6 0 1 .4 1 1 0 1.3.2 2.5.6 3.6.1.3 0 .7-.2 1z"/></svg>
    888-530-2716
  </div>
  <div class="abs tools">
    <svg width="15" height="15" viewBox="0 0 24 24"><circle cx="10" cy="10" r="7" fill="none" stroke="#555" stroke-width="2"/><path d="M15 15l6 6" stroke="#555" stroke-width="2"/></svg>
    <span style="color:#ccc">|</span>
    <svg width="14" height="14"><circle cx="7" cy="7" r="5" fill="#555"/></svg>
    <svg width="14" height="14"><circle cx="7" cy="7" r="5" fill="#555"/></svg>
    <svg width="14" height="14"><rect x="2" y="2" width="10" height="10" rx="3" fill="none" stroke="#555" stroke-width="1.6"/></svg>
  </div>
</div>

<svg class="abs hero-photo" viewBox="0 0 780 600" role="img" aria-label="Photograph of two consultants discussing work at a laptop">
  <defs>
    <linearGradient id="heroG" x1="0" y1="0" x2="1" y2="1">
      <stop offset="0" stop-color="#3f6fa3"/>
      <stop offset=".45" stop-color="#7d8fa6"/>
      <stop offset=".75" stop-color="#5a4a4a"/>
      <stop offset="1" stop-color="#2c3140"/>
    </linearGradient>
  </defs>
  <path d="M0 0H780V600C690 590 600 560 520 520C420 470 360 500 300 470C210 420 170 330 140 230C110 130 70 40 0 0Z" fill="url(#heroG)"/>
  <path d="M300 470C360 500 420 470 520 520C600 560 690 590 780 600V640H300Z" fill="#eef3f8" opacity=".7"/>
</svg>

<div class="brand" style="left:98px;top:86px;font-size:30px"><i style="width:18px;height:18px"></i>TARNWICK</div>

<nav class="nav">
  <a style="left:614px;top:80px">Home</a>
  <a style="left:683px;top:80px">About</a>
  <a style="left:751px;top:80px">Services ⌄</a>
  <a style="left:849px;top:80px">Blog</a>
</nav>
<div class="abs cta">Contact with Us</div>

<h1 class="abs head hero-title"><b>Innovative<br>EPM Solutions</b> for<br>Finance &amp; Beyond</h1>
<p class="abs hero-copy">Tarnwick Consulting provides decades of experience implementing Orvane EPM products with unique and innovative solutions</p>
<div class="btn" style="left:94px;top:515px;width:183px;height:48px">LEARN MORE →</div>

<svg class="abs" style="left:590px;top:590px" width="20" height="32" viewBox="0 0 20 32"><rect x="1" y="1" width="18" height="30" rx="9" fill="none" stroke="#9aa0aa" stroke-width="1.5"/><line x1="10" y1="7" x2="10" y2="12" stroke="#9aa0aa" stroke-width="1.5"/></svg>

<h2 class="abs head why-title"><b>Why Choose</b> Us?</h2>
<div class="rule" style="left:178px;top:815px;width:132px"></div>
<p class="abs why-copy">Tarnwick Consulting was founded on the principles of innovation and teamwork.&nbsp; We innovate the products we implement through a combination of functional expertise and technical expertise.&nbsp; When we find limitations in the products that we implement, we see this as an opportunity and a challenge to extend those products until we meet the needs of our clients.&nbsp; Through this innovation we have created various tools to accelerate our implementations.</p>
<div class="btn" style="left:178px;top:1042px;width:165px;height:46px">LEARN MORE →</div>
<div class="abs why-shadow"></div>
<div class="abs why-art" role="img" aria-label="Illustration of a digital technology collage with data icons"></div>

<svg class="abs services" viewBox="0 0 1200 690" preserveAspectRatio="none">
  <defs>
    <linearGradient id="svcG" x1="0" y1="0" x2="1" y2="1">
      <stop offset="0" stop-color="#2b74c9"/>
      <stop offset=".5" stop-color="#2878d4"/>
      <stop offset="1" stop-color="#2f6fc4"/>
    </linearGradient>
  </defs>
  <path d="M0 120L785 11L1200 107V690H0Z" fill="url(#svcG)"/>
  <path d="M0 120L785 11L790 2L0 113Z" fill="#1b5ea8"/>
</svg>
<h2 class="abs svc-title">Our Services</h2>
<div class="rule" style="left:533px;top:1442px;width:133px;background:#fff"></div>

<div class="card" style="left:172px">
  <svg width="90" height="86" viewBox="0 0 90 86" fill="none" stroke="#3a3f5a" stroke-width="2.2">
    <ellipse cx="62" cy="16" rx="16" ry="5"/><path d="M46 16v22c0 3 7 5 16 5s16-2 16-5V16M46 27c0 3 7 5 16 5s16-2 16-5"/>
    <circle cx="52" cy="40" r="12" stroke="#1b75bc"/><text x="47" y="46" font-size="16" fill="#1b75bc" stroke="none" font-family="Poppins">$</text>
    <path d="M30 26V6M24 12l6-6 6 6" stroke="#1b75bc"/>
    <path d="M4 70l14-12h18l14 6c3 2 1 6-2 5l-14-4M14 78l12-6h18l24-14c3-2 6 2 3 5L48 80H20"/>
  </svg>
  <h3>Budgeting and Forecasting</h3>
  <p>Sed ut perspiciatis unde omnis iste voluptatem accusantium doloremque laudantium, totam rem aperiam, eaque ipsa</p>
</div>
<div class="card dark" style="left:465px">
  <svg width="90" height="86" viewBox="0 0 90 86" fill="none" stroke="#fff" stroke-width="2.4">
    <path d="M6 4h26v10a6 6 0 1 0 0 10v12H20a6 6 0 1 0-10 0H6z"/>
    <path d="M36 14h26v22H50a6 6 0 1 1-10 0h-4z"/>
    <path d="M20 40h16v10a6 6 0 1 1 0 10v20H20z"/>
    <path d="M40 50h22v30H40V64a6 6 0 1 0 0-8z"/>
  </svg>
  <h3 style="margin-top:12px">Close and Consolidation</h3>
  <p style="margin-top:10px">Sed ut perspiciatis unde omnis iste voluptatem accusantium doloremque laudantium, totam rem aperiam, eaque ipsa</p>
  <svg width="22" height="18" viewBox="0 0 22 18" style="margin-top:14px"><path d="M2 9h17M12 2l7 7-7 7" fill="none" stroke="#fff" stroke-width="2.4"/></svg>
</div>
<div class="card" style="left:758px">
  <svg width="90" height="86" viewBox="0 0 90 86" fill="none" stroke="#3a3f5a" stroke-width="2.2">
    <circle cx="36" cy="36" r="26"/><circle cx="36" cy="36" r="19" stroke="#1b75bc"/>
    <path d="M24 42l8-8 6 5 10-12" stroke="#1b75bc"/>
    <path d="M54 56l20 20-6 6-20-20"/><path d="M62 18l16-14M72 4h6v6"/>
  </svg>
  <h3>Reporting and Analysis</h3>
  <p>Sed ut perspiciatis unde omnis iste voluptatem accusantium doloremque laudantium, totam rem aperiam, eaque ipsa</p>
</div>

<svg class="abs values-bg" viewBox="0 0 1200 640" preserveAspectRatio="none">
  <path d="M0 0H1200V640C980 630 760 600 560 520C430 470 380 420 300 330C220 240 260 120 120 60C70 40 30 30 0 30Z" fill="#f0f4f8"/>
</svg>
<h2 class="abs values-title">Our Core Values<br>Provide Our Foundation</h2>
<div class="rule" style="left:530px;top:2133px;width:134px"></div>

<svg class="abs" style="left:465px;top:2166px" width="268" height="268" viewBox="0 0 268 268">
  <circle cx="134" cy="134" r="106" fill="#eef2f7" stroke="#d3dae4" stroke-width="1.5"/>
  <path d="M28 134a106 106 0 0 0 212 0" fill="none" stroke="#1b75bc" stroke-width="0"/>
  <path d="M30 60A128 128 0 1 0 238 60" fill="none" stroke="#1b75bc" stroke-width="4"/>
  <circle cx="40" cy="55" r="5" fill="#fff" stroke="#1b75bc" stroke-width="1.5"/>
  <circle cx="228" cy="55" r="5" fill="#fff" stroke="#1b75bc" stroke-width="1.5"/>
  <circle cx="20" cy="190" r="5" fill="#fff" stroke="#1b75bc" stroke-width="1.5"/>
  <circle cx="248" cy="190" r="5" fill="#fff" stroke="#1b75bc" stroke-width="1.5"/>
  <text x="134" y="142" text-anchor="middle" font-family="League Spartan, sans-serif" font-weight="600" font-size="26" fill="#1b75bc">TARNWICK</text>
</svg>

<div class="val r" style="left:170px;top:2184px"><h4>Clients First</h4><p>Always do the right thing for the client, no exceptions</p></div>
<svg class="abs" style="left:387px;top:2192px" width="54" height="56" viewBox="0 0 54 56" fill="none" stroke="#3a3f5a" stroke-width="1.8"><circle cx="12" cy="8" r="5" stroke="#1b75bc"/><circle cx="27" cy="6" r="5" stroke="#1b75bc"/><circle cx="42" cy="8" r="5" stroke="#1b75bc"/><path d="M4 24c0-6 4-9 8-9s8 3 8 9M19 22c0-6 4-9 8-9s8 3 8 9M34 24c0-6 4-9 8-9s8 3 8 9"/><path d="M2 36l12-6 10 4 8-4 20 8-10 14-14-8-12 6z"/></svg>

<div class="val r" style="left:170px;top:2325px"><h4>Innovation</h4><p>Never satisfied with product limitations, we always find a way</p></div>
<svg class="abs" style="left:387px;top:2333px" width="54" height="60" viewBox="0 0 54 60" fill="none" stroke="#3a3f5a" stroke-width="1.8"><circle cx="30" cy="20" r="10" stroke="#1b75bc"/><path d="M26 30v6h8v-6" stroke="#1b75bc"/><path d="M30 2v4M16 8l3 3M44 8l-3 3"/><path d="M2 48l12-8h14l8 4h12c3 0 3 5 0 5H30l-12 8H4"/></svg>

<svg class="abs" style="left:766px;top:2192px" width="56" height="56" viewBox="0 0 56 56" fill="none" stroke="#3a3f5a" stroke-width="1.8"><rect x="2" y="2" width="8" height="8" stroke="#1b75bc"/><rect x="2" y="16" width="8" height="8" stroke="#1b75bc"/><path d="M16 6h18M16 20h14"/><path d="M4 52V40h8v12M16 52V34h8v18M28 52V38h8v14"/><path d="M40 30c6 0 10 4 10 10v12H36"/></svg>
<div class="val" style="left:835px;top:2184px"><h4>Integrity</h4><p>Always do the right thing for the client, no exceptions</p></div>

<svg class="abs" style="left:766px;top:2340px" width="58" height="58" viewBox="0 0 58 58" fill="none" stroke="#3a3f5a" stroke-width="1.8"><circle cx="29" cy="29" r="13"/><circle cx="29" cy="29" r="6" stroke="#1b75bc"/><circle cx="7" cy="7" r="4" stroke="#1b75bc"/><circle cx="51" cy="7" r="4" stroke="#1b75bc"/><circle cx="7" cy="51" r="4" stroke="#1b75bc"/><circle cx="51" cy="51" r="4" stroke="#1b75bc"/><path d="M10 10l9 9M48 10l-9 9M10 48l9-9M48 48l-9-9"/></svg>
<div class="val" style="left:835px;top:2332px"><h4>Teamwork</h4><p>Always do the right thing for the client, no exceptions</p></div>

<h2 class="abs head blog-title"><b>From The</b> Blog</h2>
<div class="rule" style="left:532px;top:2645px;width:135px;background:#6f78c9"></div>

<article class="post" style="left:172px">
  <div class="img" role="img" aria-label="Photograph of hands holding a newspaper beside a phone and coffee" style="background:linear-gradient(135deg,#4a4d52,#8a8c8f 50%,#e4e4e2)"></div>
  <div class="badge">OCT<br>2024</div>
  <div class="body">
    <h5>Orvane Cloud EPM Updates – October 2022</h5>
    <div class="by"><svg width="10" height="11"><circle cx="5" cy="3" r="3" fill="#1b75bc"/><path d="M0 11c0-4 2-6 5-6s5 2 5 6z" fill="#1b75bc"/></svg>Mara Ellison</div>
    <p>Sed ut perspiciatis unde omnis iste natus error sit voluptatem accustium dlorue laum</p>
    <div class="more">LERN MORE →</div>
  </div>
</article>
<article class="post" style="left:465px">
  <div class="img" role="img" aria-label="Award winners graphic with gold stars on a dark background" style="background:radial-gradient(circle at 50% 55%,#6a5a3a,#1a1f4a 70%)"></div>
  <div class="badge">OCT<br>2024</div>
  <div class="body">
    <h5>Encore Webinar of Konflux22’s Overall Top</h5>
    <div class="by"><svg width="10" height="11"><circle cx="5" cy="3" r="3" fill="#1b75bc"/><path d="M0 11c0-4 2-6 5-6s5 2 5 6z" fill="#1b75bc"/></svg>Owen Halvorsen</div>
    <p>Sed ut perspiciatis unde omnis iste natus error sit voluptatem accustium dlorue laum</p>
    <div class="more">LERN MORE →</div>
  </div>
</article>
<article class="post" style="left:758px">
  <div class="img" role="img" aria-label="Illustration of a hand over glowing data charts" style="background:linear-gradient(160deg,#0e2a4c,#1c5a8c 55%,#5fb3d9)"></div>
  <div class="badge">OCT<br>2024</div>
  <div class="body">
    <h5>Workforce Planning Can Be Groovy</h5>
    <div class="by"><svg width="10" height="11"><circle cx="5" cy="3" r="3" fill="#1b75bc"/><path d="M0 11c0-4 2-6 5-6s5 2 5 6z" fill="#1b75bc"/></svg>Reid Caldwell</div>
    <p>Sed ut perspiciatis unde omnis iste natus error sit voluptatem accustium dlorue laum</p>
    <div class="more">LERN MORE →</div>
  </div>
</article>

<footer>
  <div class="abs footer"></div>
  <div class="brand" style="left:170px;top:3380px;font-size:36px;color:#2f86d6"><i style="width:20px;height:20px;background:#2f86d6"></i>TARNWICK</div>
  <div class="social" style="left:173px"></div>
  <div class="social" style="left:212px"></div>
  <div class="social" style="left:250px"></div>
  <div class="social" style="left:288px"></div>

  <div class="abs f-h" style="left:486px;top:3274px">LINKS</div>
  <div class="f-links">
    <a style="top:3316px">Home</a>
    <a style="top:3348px">About us</a>
    <a style="top:3380px">Services</a>
    <a style="top:3412px">Blog</a>
    <a style="top:3444px">Contact</a>
  </div>

  <div class="abs f-h" style="left:744px;top:3271px">SIGN UP TO RECEIVE EMAIL</div>
  <p class="abs f-copy">Excepteur sint occaecat cupidatat non proident, sunt in culpa qui Nemo enim ipsam</p>
  <div class="abs f-input">Enter Email</div>
  <div class="btn" style="left:744px;top:3433px;width:118px;height:34px;font-size:13px">SUBSCRIBE</div>

  <div class="abs foot-bar">Copyright © Tarnwick Consulting 2024. All rights reserved. | Privacy Policy</div>
</footer>

</body>
</html>
```